Cowboy Ned
Cowboy Ned -
Professional
"Cowboy Ned" Hollins, Broker/Owner
Cowboy Ned Realty, LLC
4382 W Juniper Ridge Ln Gilbert, AZ 85297 (Address to be in smaller letters so as not to stand out)
Ned@CowboyNedRealty.example
www.CowboyNedRealty.example
Blog: http://housetalkhub.example/blogs/cowboyned Logo will be uploaded and should be on the front of the card. It may take up the whole front, or the front may include my phone and fax number. KTM, uDOM, FHLS, VOT Those designations above are to be added under my name.
The back will have possibly my head shot plus the contact information, web sites, etc and a couple of required Homeward logos scaled very small so as to hardly be noticeable.

```html
<!DOCTYPE html>
<html lang="en">
<head>
<meta charset="utf-8">
<title>Cowboy Ned Realty – Business Card</title>
<link href="https://fonts.googleapis.com/css2?family=Tinos:wght@400;700&family=Arimo:wght@400&display=swap" rel="stylesheet">
<style>
  :root {
    --backdrop: #e9e6e4;
    --card: #ffffff;
    --blue: #1f73b7;
    --blue-deep: #1a5f9c;
    --orange: #e0902a;
    --photo-top: #8a8f99;
    --photo-bottom: #3b3f48;
    --badge: #9aa7b8;
  }
  * { margin: 0; padding: 0; box-sizing: border-box; }
  html, body { width: 1200px; height: 901px; overflow: hidden; }
  body { background: var(--backdrop); position: relative; font-family: "Arimo", Arial, sans-serif; }

  .card {
    position: absolute;
    background: var(--card);
    box-shadow: 0 2px 10px rgba(0,0,0,0.15);
  }

  /* Front */
  .card-front { left: 68px; top: 34px; width: 718px; height: 404px; }
  .front-rule { position: absolute; left: 28px; right: 28px; background: var(--blue); }
  .front-rule.top { top: 30px; height: 4px; }
  .front-rule.bottom { bottom: 32px; height: 7px; }
  .brand {
    position: absolute; left: 70px; top: 120px;
    display: flex; align-items: center; gap: 34px;
  }
  .brand-mark {
    width: 160px; height: 160px; border-radius: 50%;
    border: 8px solid var(--orange);
  }
  .brand-name {
    font-family: "Tinos", "Times New Roman", serif;
    font-weight: 400; font-size: 54px; line-height: 1.05;
    color: var(--blue); text-transform: uppercase;
  }

  /* Back */
  .card-back { left: 462px; top: 477px; width: 716px; height: 404px; }
  .headshot {
    position: absolute; left: 28px; top: 14px; width: 134px; height: 160px;
    border: 4px solid var(--orange); border-radius: 8px;
    background: linear-gradient(180deg, var(--photo-top), var(--photo-bottom));
  }
  .agent-name {
    position: absolute; left: 174px; top: 58px;
    font-family: "Tinos", "Times New Roman", serif;
    font-size: 28px; color: var(--blue-deep); white-space: nowrap;
  }
  .name-rule {
    position: absolute; left: 164px; right: 0; top: 98px; height: 5px;
    background: linear-gradient(90deg, var(--blue) 0%, var(--blue) 85%, rgba(31,115,183,0.2) 100%);
  }
  .designations {
    position: absolute; right: 30px; top: 114px;
    font-family: "Tinos", "Times New Roman", serif;
    font-size: 19px; letter-spacing: 3px; color: var(--orange);
  }
  .contact {
    position: absolute; left: 28px; top: 202px;
    list-style: none; color: var(--orange); font-size: 18px; line-height: 25px;
  }
  .footer-rule { position: absolute; left: 12px; right: 12px; }
  .footer-rule.blue { top: 336px; height: 3px; background: var(--blue); }
  .footer-rule.orange { top: 344px; height: 4px; background: var(--orange); }
  .affiliations { position: absolute; left: 28px; top: 366px; display: flex; gap: 8px; }
  .badge { width: 22px; height: 16px; background: var(--badge); }
  .badge.square { width: 16px; }
  .address {
    position: absolute; right: 30px; top: 368px;
    font-size: 13px; color: var(--orange);
  }
</style>
</head>
<body>
  <section class="card card-front">
    <div class="front-rule top"></div>
    <div class="brand">
      <div class="brand-mark"></div>
      <div class="brand-name">Cowboy Ned<br>Realty, LLC</div>
    </div>
    <div class="front-rule bottom"></div>
  </section>

  <section class="card card-back">
    <div class="headshot" role="img" aria-label="Headshot of Cowboy Ned Hollins"></div>
    <h1 class="agent-name" style="font-weight:400">“Cowboy Ned” Hollins, Broker/Owner</h1>
    <div class="name-rule"></div>
    <p class="designations">KTM, uDOM, FHLS, VOT</p>
    <ul class="contact">
      <li>Cell: (555) 014 2730</li>
      <li>Fax: (555) 014 2981</li>
      <li>Email: Ned@CowboyNedRealty.example</li>
      <li>Web: www.CowboyNedRealty.example</li>
      <li>Blog: http://housetalkhub.example/blogs/cowboyned</li>
    </ul>
    <div class="footer-rule blue"></div>
    <div class="footer-rule orange"></div>
    <div class="affiliations">
      <span class="badge"></span>
      <span class="badge square"></span>
    </div>
    <p class="address">4382 W Juniper Ridge Ln :: Gilbert, AZ 85297</p>
  </section>
</body>
</html>
```